Paws Home

Need Yard signs
Dimensions 24" wide and 18" high

Copy: Rescue does not mean "Damaged". It means they have been let down by humans.
Please adopt at: 217 W Brannock Ave, Tampa, Fl 33682
Open: Tues-Sun 10am - 7pm

I have attached a sample of the original ad. I can't use this because the resolution is too low and the type has to be big enough so that it can be seen 12 feet away.
I have also attached some photos you can use. The res may not be hi enough, but perhaps you can find some stock photography even these pics are not hi res enough.

Target Market(s)

animal lovers

Font styles to use
Sans Serif

Colors

Designer to choose colors to be used in the design.

Requirements
Must have
• Must be easy to read.

```html
<!DOCTYPE html>
<html lang="en">
<head>
<meta charset="utf-8">
<title>Paws Home – Yard Sign</title>
<link href="https://fonts.googleapis.com/css2?family=Anton&family=Oswald:wght@600;700&family=Roboto:wght@700&family=Roboto+Condensed:wght@700&display=swap" rel="stylesheet">
<style>
  :root {
    --ink: #000000;
    --sign-yellow: #ffd400;
    --sign-white: #ffffff;
    --band-red: #9a1b1f;
    --fur-warm: #b86a3a;
    --fur-light: #e2c39a;
  }
  * { margin: 0; padding: 0; box-sizing: border-box; }
  html, body {
    width: 1200px; height: 900px; overflow: hidden; background: var(--ink);
  }
  .sign {
    position: relative; width: 1200px; height: 900px; overflow: hidden;
    background: var(--ink);
  }
  .dog-photo {
    position: absolute; left: 540px; top: 110px; width: 660px; height: 642px;
    background:
      radial-gradient(ellipse 55% 50% at 55% 55%, var(--fur-light) 0%, var(--fur-warm) 45%, rgba(90,40,20,0.6) 70%, rgba(0,0,0,0) 100%);
  }
  .headline {
    position: absolute; left: 70px; top: 78px;
    font-family: "Roboto", Arial, sans-serif; font-weight: 700;
    font-size: 90px; line-height: 110px; color: var(--sign-yellow);
    letter-spacing: -0.5px;
  }
  .headline-accent {
    position: absolute; left: 68px; top: 292px;
    font-family: "Anton", Impact, sans-serif; font-size: 168px; line-height: 168px;
    color: var(--sign-yellow); transform: scaleX(0.82); transform-origin: left top;
    letter-spacing: 2px;
  }
  .message {
    position: absolute; left: 68px; top: 505px;
    font-family: "Roboto Condensed", Arial Narrow, sans-serif; font-weight: 700;
    font-size: 56px; line-height: 68px; color: var(--sign-white);
  }
  .info-band {
    position: absolute; left: 0; top: 752px; width: 1200px; height: 126px;
  }
  .info-band svg { position: absolute; left: 0; top: 0; }
  .adopt-label {
    position: absolute; left: 57px; top: 774px;
    font-family: "Oswald", Arial Narrow, sans-serif; font-weight: 700;
    font-size: 56px; line-height: 76px; color: var(--sign-yellow);
    transform: scaleX(0.86); transform-origin: left center; letter-spacing: -1px;
  }
  .address, .hours {
    position: absolute; right: 44px; text-align: right;
    font-family: "Roboto Condensed", Arial Narrow, sans-serif; font-weight: 700;
    white-space: nowrap;
  }
  .address { top: 766px; font-size: 36px; color: var(--sign-white); letter-spacing: 0.5px; }
  .hours { top: 817px; font-size: 40px; color: var(--sign-yellow); letter-spacing: 0.5px; }
</style>
</head>
<body>
<main class="sign">
  <div class="dog-photo" role="img" aria-label="Photo of a sad golden dog resting its head on its paws behind a chain-link fence"></div>

  <h1 class="headline">RESCUE DOES<br>NOT MEAN</h1>
  <p class="headline-accent">“DAMAGED.”</p>

  <p class="message">IT MEANS THEY HAVE<br>BEEN LET DOWN<br>BY HUMANS.</p>

  <div class="info-band">
    <svg width="1200" height="126" viewBox="0 0 1200 126" aria-hidden="true">
      <rect x="0" y="0" width="1200" height="2" fill="var(--sign-yellow)"/>
      <polygon points="0,8 456,8 504,120 0,120" fill="var(--band-red)"/>
      <rect x="0" y="124" width="1200" height="2" fill="var(--sign-yellow)"/>
    </svg>
  </div>
  <p class="adopt-label">PLEASE ADOPT AT</p>
  <p class="address">217 W BRANNOCK AVE, TAMPA, FL 33682</p>
  <p class="hours">OPEN: TUES-SUN 10AM - 7PM</p>
</main>
</body>
</html>
```